Etiketten für Basenpulver
Zielgruppe
Das Produkt ist ein Basenpulver, das Etikett sollte aber genauso gut für alle anderen Nahrungsergänzungsmittel einsetzbar sein.
Edles, seriöses Produkt, welches von Naturheilpraktikern und Ärzten empfohlen werden kann.
Soll trotzdem eine Assoziation von Lebendigkeit (Lebhaft) und Vita(-lisierend) drin haben.
Aufgabenstellung
Das Etikett ist für ein Basenpulver, das Grunddesign sollte jedoch auch für andere Nahrungsergänzungsmittel produkte funktionieren.
Die Verpackung ist eine 300g weiße Schraubverschluss Dose:
die Höhe des Etiketts: 67,7mm
die länge kann zwischen 97mm und 200mm variieren, je nach design.
Gerne auch zwei einzelne Etiketten mit jeweils den Maßen: 97mm * 67,7mm

```html
<!DOCTYPE html>
<html lang="de">
<head>
<meta charset="utf-8">
<title>Basenpulver Etikett</title>
<link rel="stylesheet" href="https://fonts.googleapis.com/css2?family=Oswald:wght@300;400;500&family=Montserrat:wght@800&family=Questrial&family=Nunito:wght@800&display=swap">
<style>
  :root {
    --green: #5aac2e;
    --green-pale: #bedca8;
    --ink: #222222;
    --frame: #555555;
    --paper: #ffffff;
  }
  * { margin: 0; padding: 0; box-sizing: border-box; }
  html, body { width: 1200px; height: 694px; overflow: hidden; background: var(--paper); }
  body { position: relative; font-family: "Oswald", sans-serif; font-weight: 300; color: var(--ink); }

  .label {
    position: absolute; left: 88px; top: 113px; width: 996px; height: 449px;
    border: 1px solid var(--frame); background: var(--paper);
  }
  .abs { position: absolute; white-space: nowrap; }

  .wave-band {
    left: 89px; top: 128px; width: 994px; height: 116px;
    background:
      radial-gradient(circle at 493px 51px, rgba(235,242,245,0.95) 0 34px, rgba(200,215,222,0.7) 36px, transparent 39px),
      linear-gradient(180deg, rgba(255,255,255,0) 0%, rgba(168,220,90,0.55) 30%, rgba(120,200,50,0.75) 55%, rgba(190,235,120,0.4) 80%, rgba(255,255,255,0) 100%);
  }

  .green { color: var(--green); font-weight: 500; }

  .ingredients { left: 101px; top: 229px; font-size: 13px; letter-spacing: -0.2px; }

  .nutrition {
    left: 100px; top: 255px; width: 259px; height: 125px;
    border: 1px solid var(--frame); background: var(--paper);
  }
  .nutrition h2 { position: absolute; left: 7px; top: 1px; font-size: 15px; font-weight: 500; color: var(--green); }
  .nutrition .row { position: absolute; left: 0; width: 100%; height: 20px; font-size: 13px; line-height: 20px; letter-spacing: -0.2px; }
  .nutrition .row.shaded { background: var(--green-pale); }
  .nutrition .row span { position: absolute; }
  .c1 { left: 6px; } .c2 { left: 62px; } .c3 { left: 121px; } .c4 { left: 172px; } .c5 { left: 228px; }

  .copy { left: 100px; font-size: 12px; line-height: 16.3px; letter-spacing: -0.25px; }
  .usage { top: 380px; }
  .notice { top: 450px; }
  .shelf { top: 523px; font-size: 13px; }

  .product-name {
    left: 385px; top: 274px; width: 400px; text-align: center;
    font-family: "Montserrat", sans-serif; font-weight: 800; font-size: 44px; letter-spacing: 0.3px; color: var(--green);
  }
  .subtitle {
    left: 385px; top: 328px; width: 400px; text-align: center;
    font-family: "Questrial", sans-serif; font-size: 20px; line-height: 25px; color: #333;
  }
  .claims {
    left: 385px; top: 373px; width: 400px; text-align: center;
    font-family: "Nunito", sans-serif; font-weight: 800; font-size: 18px; color: var(--green);
  }

  .brand {
    left: 470px; top: 576px; width: 230px; display: flex; align-items: center; justify-content: center; gap: 8px;
    font-family: "Oswald", sans-serif; font-weight: 500; font-size: 26px; color: var(--green); letter-spacing: 1px;
  }
  .brand-dot { width: 16px; height: 16px; border-radius: 50%; background: var(--green); }

  .benefit-intro { left: 817px; top: 236px; font-size: 14px; line-height: 18.5px; letter-spacing: -0.2px; }

  .badge { width: 56px; height: 56px; border-radius: 50%; background: var(--green); top: 285px; }
  .badge-caption { top: 346px; width: 90px; text-align: center; font-size: 12.5px; line-height: 17px; letter-spacing: -0.2px; }

  .maker { left: 817px; top: 411px; font-size: 14.5px; line-height: 19.7px; letter-spacing: -0.2px; }
  .amount { left: 817px; top: 492px; font-size: 21px; font-weight: 400; }
  .amount .green { font-weight: 500; }
</style>
</head>
<body>
  <div class="label"></div>

  <p class="abs benefit-intro">Zink trägt zu einem normalen Säuren-Basen-Stoffwechsel<br>bei. Unterstützung gegen Übersäuerung.</p>

  <div class="abs wave-band" role="img" aria-label="Geschwungene hellgrüne Bänder mit einer klaren Wasserperle in der Mitte"></div>

  <p class="abs ingredients"><span class="green">Inhalt:</span> Kaliumcitrat, Calciumcitrat, Magnesiumcitrat</p>

  <section class="abs nutrition">
    <h2>Nährwerttabelle:</h2>
    <div class="row shaded" style="top:24px"><span class="c1">Inhalt pro:</span><span class="c2">1ml=4,5g</span><span class="c3">%NRV</span><span class="c4">2ml=9g</span><span class="c5">%NRV</span></div>
    <div class="row" style="top:44px"><span class="c1">Kalium</span><span class="c2">648mg</span><span class="c3">32,4</span><span class="c4">1296mg</span><span class="c5">64,8</span></div>
    <div class="row shaded" style="top:64px"><span class="c1">Calcium</span><span class="c2">378mg</span><span class="c3">42,25</span><span class="c4">756mg</span><span class="c5">84,5</span></div>
    <div class="row" style="top:86px"><span class="c1">Magnesium</span><span class="c2">144mg</span><span class="c3">38,4</span><span class="c4">288mg</span><span class="c5">76,8</span></div>
  </section>

  <p class="abs copy usage"><span class="green">Verzehrsempfehlung:</span> 1-2 mal 1 gestrichenen Mess- löffel á<br>4,5g in 300ml natiumarmen Sprudel/Wasser auflösen. Am besten zu<br>Mahlzeiten trinken. Für die richtige Dosierung <span class="green">vor jedem Öffnen</span><br><span class="green">schütteln!</span></p>

  <p class="abs copy notice">Wichtiger Hinweis: Nahrungsergänzungsmittel sind kein Ersatz für eine<br>ausgewogene und abwechslungsreiche Ernährung sowie eine gesunde<br>Lebensweise. Die empfohlene Verzehrmenge nicht überschreiten.<br>Außerhalb der Reichweite von kleinen Kindern aufbewahren.</p>

  <p class="abs copy shelf"><span class="green">Mindestens haltbar bis: siehe Boden</span></p>

  <h1 class="abs product-name">BASENPULVER</h1>
  <p class="abs subtitle">Mit basischen Mineralstoffen und Zink<br>für die Säuren-Basen-Ballance</p>
  <p class="abs claims">Vegan / Glutenfrei / Laktosefrei</p>

  <div class="abs brand"><span class="brand-dot"></span>VIREO KRÄUTER</div>

  <div class="abs badge" style="left:836px"></div>
  <div class="abs badge" style="left:913px"></div>
  <div class="abs badge" style="left:992px"></div>
  <p class="abs badge-caption" style="left:819px">Keine künstlichen<br>Aromen oder<br>Süßungsmittel</p>
  <p class="abs badge-caption" style="left:896px">Natriumarm<br>und<br>kaliumreich</p>
  <p class="abs badge-caption" style="left:975px">Frei von<br>Zusatzstoffen</p>

  <p class="abs maker">Hergestellt in Deutschland<br>Vireo - Quelle der Kräuter - Lindenpfad 12<br>54321 Kräuterfeld - www.vireo-kraeuter.de</p>

  <p class="abs amount"><span class="green">Inhalt 360g</span> = 60 Portionen</p>
</body>
</html>
```